BRC Business cards

We are a medium sized property company based in London and require a logo, Business card which reflects a professional company and incorporates our catchy name.

Our statement is (Building for the future) we like colours such as royal blue, greens and light browns but will look at anything.

Contact Information for Business Card

Brookcrest Estates Limited
Unit 4, 15-17 Farrowby Lane
London
SE22 7QN

Web: www.brookcrestestates-example.com

Email: brookcrestltd@mailbox-example.com

Telephone: +44-208-555-0142
Fax: +44-208-555-0187

```html
<!DOCTYPE html>
<html lang="en">
<head>
<meta charset="utf-8">
<title>Brookcrest Estates Limited – Business Card</title>
<link rel="stylesheet" href="https://fonts.googleapis.com/css2?family=Arimo:wght@400&family=Tinos:wght@700&display=swap">
<style>
  :root {
    --brand-red: #c00000;
    --brand-red-soft: #d42a2a;
    --brand-red-pale: #f3d2d2;
    --paper: #ffffff;
    --text-light: #ffffff;
  }
  * { margin: 0; padding: 0; box-sizing: border-box; }
  html, body { width: 1200px; height: 686px; overflow: hidden; background: var(--paper); }
  .card { position: relative; width: 1200px; height: 686px; background: var(--paper); overflow: hidden; }
  .card-art { position: absolute; inset: 0; width: 1200px; height: 686px; }
  .mark-area { position: absolute; left: 735px; top: 300px; width: 443px; height: 366px; }
  .company-name {
    position: absolute; right: 369px; top: 62px;
    font-family: "Tinos", "Times New Roman", serif; font-weight: 700;
    font-size: 53px; line-height: 64px; color: var(--text-light); text-align: right;
  }
  .contact-line {
    position: absolute; left: 40px;
    font-family: "Arimo", Arial, sans-serif; font-weight: 400;
    color: var(--text-light); font-size: 28px; line-height: 36px; white-space: nowrap;
  }
  .contact-address { top: 392px; left: 21px; width: 390px; text-align: center; }
  .contact-phone { top: 482px; }
  .contact-email { top: 575px; }
</style>
</head>
<body>
<main class="card">
  <svg class="card-art" viewBox="0 0 1050 600" preserveAspectRatio="none" aria-hidden="true">
    <polygon class="headline-panel" fill="var(--brand-red)"
      points="20,18 1030,18 1030,230 590,545"/>
    <g class="contact-tabs" fill="var(--brand-red)">
      <polygon points="18,342 355,342 415,410 18,410"/>
      <polygon points="18,418 355,418 415,487 18,487"/>
      <polygon points="18,492 470,492 520,540 18,540"/>
    </g>
  </svg>

  <svg class="mark-area" viewBox="0 0 443 366" preserveAspectRatio="none" role="img" aria-label="Company house mark">
    <defs>
      <linearGradient id="mark-fill" x1="0" y1="0" x2="1" y2="0">
        <stop offset="0" stop-color="var(--brand-red-soft)"/>
        <stop offset="1" stop-color="var(--brand-red-pale)"/>
      </linearGradient>
    </defs>
    <rect width="443" height="366" fill="url(#mark-fill)"/>
  </svg>

  <h1 class="company-name">Brookcrest Estates<br>Limited</h1>

  <p class="contact-line contact-address">4, 15-17 Farrowby<br>Lane London SE22 7QN</p>
  <p class="contact-line contact-phone">Ph:+44-208-555-0142<br>Fax: +44-208-555-0187</p>
  <p class="contact-line contact-email">brookcrestltd@mailbox-example.com</p>
</main>
</body>
</html>
```